Gordon Pellbrook Consulting - Web Design Project

We need a web design for my new edgy consulting business specializing in innovation, technology and strategy.

It is our personal goal to turn each client into raving fans by helping them achieve their own business goals and aspirations through assisting them in raising their own innovation and marketing standards.

We provide our personalised and state-of-the-art services to our clients and boards who represent some of the world greatest innovative thinkers.
Updates

Here is some other information which may help shape your thinking.

I've had direct Involvement in the development of the following iPad, iPhone Applications and websites

FarbeyondOzlands.com (TerraLink platform) by Voyage Bureau
http://farbeyondozlands.example.au

Sail Verve by Bright Voyaging
https://apps.example-store.com/au/app/sail-verve/id100000001

uRedlandTR by Travel Territory Board
https://apps.example-store.com/au/app/uredlandtr/id100000002

Wexmoor Trips
http://www.wexmoortrips.example.au

Trek Mapper by Voyage Bureau
http://apps.example-store.com/au/app/trek-mapper/id100000003

Sunward by Sunward Travel Office
https://apps.example-store.com/au/app/sunward/id100000004

Upper Fernridge Valley Route by Visit Coastlands
https://apps.example-store.com/au/app/upper-fernridge-valley-route/id100000005

Wanderer Path by Travel Territory Board and Southern Plains Travel Council
https://apps.example-store.com/au/app/wanderers-path-grand-journey/id100000006

Gordon Pellbrook Consulting (GPC)
November 2012 – Present (8 months)Brisbane, Sydney, Canberra

Gordon’s consults to Small-to-Medium Enterprises (SME) and Government organisations on business strategy, technology strategy, risk mitigation, disruptive technology and innovation in the workplace.

Gordon’s consultancy mantra is that we cannot divorce economic life from cultural life particularly in an era when social capital may be as important as physical capital in business.

Reason: request from designers, I want to see their best efforts

Target Market(s)

35+

Industry/Entity Type

Business

Requirements
Must have
• Please use some of the personal image(s) contained in the zip files which can be downloaded from here

http://filedrop.example/k9Xq2Lm
http://filedrop.example/p4Rt7Vn
http://filedrop.example/z8Hw3Bc
Nice to have
• Black, Sleek design, maybe minimalist. Nice to have a Pixelle for the design. Nice to have it easily ported to Wordpress or be a modified Wordpress template. HTML 5, responsive design

```html
<!DOCTYPE html>
<html lang="en">
<head>
<meta charset="utf-8">
<title>Gordon Pellbrook Consulting</title>
<link rel="stylesheet" href="https://fonts.googleapis.com/css2?family=Open+Sans:wght@300;400;600&family=Tinos&family=Arimo:wght@400;700&display=swap">
<style>
  :root {
    --page-bg: #f3f3f3;
    --header-top: #000000;
    --header-bottom: #2a2a2a;
    --field-bg: #1c1c1c;
    --field-border: #3a3a3a;
    --field-text: #7a7a7a;
    --login-blue: #1a6fd0;
    --brand-blue: #0c4a86;
    --brand-blue-light: #1c5f9e;
    --label-blue: #2d5f91;
    --hero-blue: #1a6dc4;
    --ink: #1e1e1e;
    --muted: #444444;
    --nav-bg: #f0f0f0;
    --white: #ffffff;
  }
  * { box-sizing: border-box; margin: 0; padding: 0; }
  html, body { width: 742px; height: 1200px; overflow: hidden; }
  body { background: var(--page-bg); font-family: "Open Sans", sans-serif; position: relative; }

  .site { position: absolute; left: 224px; top: 0; width: 286px; height: 1200px; background: var(--white); }

  .site-header {
    position: absolute; left: 0; top: 0; width: 286px; height: 195px;
    background: linear-gradient(180deg, var(--header-top) 0%, #0e0e0e 55%, var(--header-bottom) 100%);
  }
  .search-bar {
    position: absolute; left: 18px; top: 5px; width: 253px; height: 19px;
    background: var(--white); border-radius: 2px;
    font: 11px "Arimo", sans-serif; color: #555; line-height: 19px; padding-left: 25px;
  }
  .search-bar svg { position: absolute; top: 4px; }
  .search-bar .search-icon { left: 7px; }
  .search-bar .mic-icon { right: 7px; }

  .login-row { position: absolute; top: 33px; left: 19px; height: 22px; }
  .login-field {
    position: absolute; top: 0; height: 22px; background: var(--field-bg);
    border: 1px solid var(--field-border); border-radius: 2px;
    font: 11px "Arimo", sans-serif; color: var(--field-text); line-height: 20px; padding-left: 5px;
  }
  .login-field.username { left: 0; width: 89px; }
  .login-field.password { left: 96px; width: 84px; }
  .login-button {
    position: absolute; left: 191px; top: 0; width: 61px; height: 22px; border-radius: 2px;
    background: linear-gradient(180deg, #3a8ee8, var(--login-blue));
    color: var(--white); font: 700 10px "Arimo", sans-serif; text-align: center; line-height: 22px;
  }

  .social-links { position: absolute; top: 76px; left: 0; width: 286px; height: 24px; }
  .social-links span {
    position: absolute; top: 2px; width: 20px; height: 20px; background: #2c2c2c;
    border: 1px solid #4a4a4a; transform: rotate(45deg);
  }

  .brand-name {
    position: absolute; right: 27px; top: 117px;
    font: 300 28px "Open Sans", sans-serif; color: var(--white); letter-spacing: 0.5px;
    text-shadow: 0 1px 0 #888;
  }
  .brand-tag {
    position: absolute; right: 27px; top: 152px;
    font: 400 17px "Open Sans", sans-serif; color: var(--white);
  }

  .phone-bar {
    position: absolute; top: 195px; left: 0; width: 286px; height: 45px;
    text-align: center; font: 27px "Tinos", serif; color: var(--ink); line-height: 45px;
  }
  .phone-bar svg { vertical-align: -1px; margin-right: 4px; }

  .main-nav {
    position: absolute; top: 247px; left: 10px; width: 271px; height: 44px;
    background: var(--nav-bg); border-radius: 4px;
  }
  .main-nav .current { position: absolute; left: 14px; top: 0; line-height: 44px; font: 400 18px "Open Sans", sans-serif; color: var(--ink); }
  .main-nav .menu-toggle { position: absolute; right: 10px; top: 6px; }

  .hero { position: absolute; top: 300px; left: 10px; width: 271px; height: 174px; }
  .hero-portrait {
    position: absolute; left: 0; top: 0; width: 102px; height: 174px;
    background: linear-gradient(180deg, #d9d4cf 0%, #2b2d33 45%, #1b1c20 100%);
    border-radius: 40px 40px 0 0;
  }
  .hero-copy { position: absolute; right: 10px; top: 38px; text-align: right; color: var(--ink); }
  .hero-copy .lead { font: 300 21px/26px "Open Sans", sans-serif; color: var(--muted); letter-spacing: -0.5px; }
  .hero-copy .strong { font: 400 26px/31px "Open Sans", sans-serif; letter-spacing: -0.8px; }
  .hero-copy .accent { font: 400 40px/44px "Open Sans", sans-serif; color: var(--hero-blue); letter-spacing: -1px; }

  .service { position: absolute; left: 0; width: 286px; text-align: center; }
  .service svg { display: block; margin: 0 auto; }
  .service-label { font: 400 20px/23px "Open Sans", sans-serif; color: var(--label-blue); margin-top: 10px; }

  .site-footer { position: absolute; left: 0; top: 1191px; width: 286px; height: 9px; background: #111; }
</style>
</head>
<body>
  <div class="site">
    <header class="site-header">
      <div class="search-bar">
        <svg class="search-icon" width="11" height="11" viewBox="0 0 11 11"><circle cx="4.5" cy="4.5" r="3.3" fill="none" stroke="#999" stroke-width="1.4"/><line x1="7" y1="7" x2="10" y2="10" stroke="#999" stroke-width="1.6"/></svg>
        Enter Keyword to search
        <svg class="mic-icon" width="8" height="11" viewBox="0 0 8 11"><rect x="2.3" y="0" width="3.4" height="6.5" rx="1.7" fill="#888"/><path d="M1 5 Q4 9 7 5" fill="none" stroke="#888" stroke-width="1"/><line x1="4" y1="8" x2="4" y2="11" stroke="#888"/></svg>
      </div>
      <div class="login-row">
        <div class="login-field username">Username</div>
        <div class="login-field password">Password</div>
        <div class="login-button">LOGIN</div>
      </div>
      <div class="social-links">
        <span style="left:96px"></span>
        <span style="left:134px"></span>
        <span style="left:172px"></span>
      </div>
      <div class="brand-name">Gordon Pellbrook</div>
      <div class="brand-tag">Consulting</div>
    </header>

    <div class="phone-bar">
      <svg width="20" height="20" viewBox="0 0 24 24"><path d="M6.6 2.5l3 3.6-2 2.4c1.4 3 4 5.6 7 7l2.4-2 3.6 3-2.2 3.2C12 19.6 4.4 12 2.4 5.6z" fill="#222"/></svg>1-000-123-4567
    </div>

    <nav class="main-nav">
      <span class="current">HOME</span>
      <svg class="menu-toggle" width="32" height="32" viewBox="0 0 32 32"><circle cx="16" cy="16" r="16" fill="#cfcfcf"/><rect x="8" y="10" width="16" height="2.4" rx="1" fill="#fff"/><rect x="8" y="15" width="16" height="2.4" rx="1" fill="#fff"/><rect x="8" y="20" width="16" height="2.4" rx="1" fill="#fff"/></svg>
    </nav>

    <section class="hero">
      <div class="hero-portrait" role="img" aria-label="Portrait of the consultant in a dark suit"></div>
      <div class="hero-copy">
        <div class="lead">you will definitely</div>
        <div class="strong">HAVE A</div>
        <div class="strong">GOOD START</div>
        <div class="accent">with us!</div>
      </div>
    </section>

    <svg width="0" height="0" style="position:absolute">
      <defs>
        <linearGradient id="hexFill" x1="0" y1="0" x2="0" y2="1">
          <stop offset="0" stop-color="#1c5f9e"/><stop offset="1" stop-color="#0a3f75"/>
        </linearGradient>
        <radialGradient id="hexShadow"><stop offset="0" stop-color="#000" stop-opacity="0.3"/><stop offset="1" stop-color="#000" stop-opacity="0"/></radialGradient>
      </defs>
    </svg>

    <div class="service" style="top:491px">
      <svg width="100" height="106" viewBox="0 0 100 106">
        <ellipse cx="50" cy="98" rx="42" ry="7" fill="url(#hexShadow)"/>
        <polygon points="50,2 95,27 95,76 50,101 5,76 5,27" fill="url(#hexFill)"/>
        <path d="M27 30 V73 H74" fill="none" stroke="#d8dce2" stroke-width="3"/>
        <polyline points="33,64 44,50 54,58 68,40" fill="none" stroke="#fff" stroke-width="3"/>
        <circle cx="44" cy="50" r="3" fill="#fff"/><circle cx="54" cy="58" r="3" fill="#fff"/>
        <polygon points="72,34 72,46 62,38" fill="#fff"/>
      </svg>
      <div class="service-label">Organisational<br>Development</div>
    </div>

    <div class="service" style="top:671px">
      <svg width="100" height="106" viewBox="0 0 100 106">
        <ellipse cx="50" cy="98" rx="42" ry="7" fill="url(#hexShadow)"/>
        <polygon points="50,2 95,27 95,76 50,101 5,76 5,27" fill="url(#hexFill)"/>
        <circle cx="50" cy="51" r="20" fill="none" stroke="#c9ced6" stroke-width="3"/>
        <circle cx="50" cy="31" r="8" fill="#fff"/>
        <circle cx="33" cy="62" r="8" fill="#d0d4da"/>
        <circle cx="67" cy="62" r="8" fill="#d0d4da"/>
      </svg>
      <div class="service-label">Audience<br>Development</div>
    </div>

    <div class="service" style="top:857px">
      <svg width="100" height="106" viewBox="0 0 100 106">
        <ellipse cx="50" cy="98" rx="42" ry="7" fill="url(#hexShadow)"/>
        <polygon points="50,2 95,27 95,76 50,101 5,76 5,27" fill="url(#hexFill)"/>
        <g fill="none" stroke="#e4e7eb" stroke-width="3">
          <circle cx="50" cy="51" r="21"/>
          <ellipse cx="50" cy="51" rx="9" ry="21"/>
          <line x1="50" y1="30" x2="50" y2="72"/>
          <line x1="29" y1="51" x2="71" y2="51"/>
          <path d="M32 40 H68 M32 62 H68"/>
        </g>
      </svg>
      <div class="service-label">Insight<br>Research</div>
    </div>

    <div class="service" style="top:1032px">
      <svg width="100" height="106" viewBox="0 0 100 106">
        <ellipse cx="50" cy="98" rx="42" ry="7" fill="url(#hexShadow)"/>
        <polygon points="50,2 95,27 95,76 50,101 5,76 5,27" fill="url(#hexFill)"/>
        <g fill="none" stroke="#e4e7eb" stroke-width="4">
          <circle cx="50" cy="51" r="21"/>
          <circle cx="50" cy="51" r="12"/>
        </g>
        <circle cx="50" cy="51" r="5" fill="#fff"/>
      </svg>
      <div class="service-label">Evaluation</div>
    </div>

    <footer class="site-footer"></footer>
  </div>
</body>
</html>
```